Design a CD Cover For Baby Music and Lullabies To Appear on Tune Harbor Shop etc.

Please read this brief before you design. Otherwise you will be wasting your time.

I need a cd cover for music albums which will appear on streaming sites such as Tune Harbor Shop Wavelane, Pluvix etc. for the brand Cozy Cradle Tunes. The thumbnails are quite small so the text needs to be quite large.

I need a design if possible, in which I can simply alter the title of the album and the baby picture so that each album has a different cover but works with the branding.

You can check out the Cozy Cradle Tunes on the Tune Harbor shop.
https://play.wavelane.example/artist/7qk3RtLmWvNx82hYbPdaZe

I made those covers and I really don't like them at all! As you can tell I am not a graphic designer. Ha.

Please help me with a modern, eye catching and cute design that will work across the brand now and in the future. The CCT logo and the name Cozy Cradle Tunes is the only thing that needs to be used somewhere in the design.

Please use the title

Soft Hush Tones For Nap Time Part First

for this first album.
(White noise sounds are hair dryers, vacuum cleaners, fans, wind, rain, the sea, white noise, pink noise, brown noise etc. )

Here is an example of album covers which are coherent. A style like this without the over the top text would be good. But don't copy these!
https://play.wavelane.example/artist/9TfKxcMnEuGh31oAsQbiR5

Target Market(s)

Parents of babies.

Font styles to use
Serif
Sans Serif

Colors

Designer to choose colors to be used in the design.

Requirements
Must have
• Large font so it can been seen in the wavelane thumbnail. A photo of a baby. Please take a look at the wavelane and tune harbor stores. The Cozy Cradle Tunes logo.
• Album Title
• Soft Hush Tones For Nap Time Part First

```html
<!DOCTYPE html>
<html lang="en">
<head>
<meta charset="utf-8">
<title>Cozy Cradle Tunes – Soft Hush Tones For Nap Time</title>
<link rel="stylesheet" href="https://fonts.googleapis.com/css2?family=Quicksand:wght@500;700&display=swap">
<style>
  :root {
    --brand-blue: #3d71b0;
    --panel-sky: #eaf2fd;
    --title-blue: #3a6db0;
    --subtitle-blue: #7c9fd9;
    --white: #ffffff;
  }
  html, body {
    margin: 0;
    padding: 0;
    width: 1200px;
    height: 1200px;
    overflow: hidden;
    background: var(--brand-blue);
  }
  .cover {
    position: relative;
    width: 1200px;
    height: 1200px;
    overflow: hidden;
    font-family: "Quicksand", sans-serif;
  }
  .cover-backdrop {
    position: absolute;
    inset: 0;
  }
  .brand-mark {
    position: absolute;
    left: 56px;
    top: 38px;
    width: 184px;
    height: 184px;
    box-sizing: border-box;
    border-radius: 50%;
    border: 3px solid var(--white);
    background: var(--brand-blue);
  }
  .brand-name {
    position: absolute;
    left: 290px;
    top: 62px;
    margin: 0;
    font-weight: 500;
    font-size: 96px;
    line-height: 1;
    color: var(--white);
    white-space: nowrap;
  }
  .album-title {
    position: absolute;
    left: 0;
    right: 0;
    top: 350px;
    margin: 0;
    text-align: center;
    font-weight: 700;
    font-size: 38px;
    letter-spacing: 3px;
    text-transform: uppercase;
    color: var(--title-blue);
  }
  .album-volume {
    position: absolute;
    left: 0;
    right: 0;
    top: 402px;
    margin: 0;
    text-align: center;
    font-weight: 500;
    font-size: 33px;
    letter-spacing: 1px;
    color: var(--subtitle-blue);
  }
  .photo-frame {
    position: absolute;
    left: 0;
    top: 0;
  }
</style>
</head>
<body>
<main class="cover">
  <svg class="cover-backdrop" width="1200" height="1200" viewBox="0 0 1200 1200" aria-hidden="true">
    <defs>
      <filter id="soft-shadow" x="-5%" y="-10%" width="110%" height="120%">
        <feDropShadow dx="0" dy="0" stdDeviation="6" flood-color="#1f3f6a" flood-opacity="0.25"/>
      </filter>
    </defs>
    <rect width="1200" height="1200" fill="var(--brand-blue)"/>
    <path class="sky-panel" filter="url(#soft-shadow)" fill="var(--panel-sky)"
          d="M0 285 Q600 255 1200 285 L1200 1150 Q600 1180 0 1150 Z"/>
  </svg>

  <div class="brand-mark"></div>
  <h1 class="brand-name">Cozy Cradle Tunes</h1>

  <h2 class="album-title">Soft Hush Tones For Nap Time</h2>
  <p class="album-volume">Part First</p>

  <svg class="photo-frame" width="1200" height="1200" viewBox="0 0 1200 1200">
    <defs>
      <radialGradient id="nest-tones" cx="0.45" cy="0.5" r="0.6">
        <stop offset="0" stop-color="#f3d2cc"/>
        <stop offset="0.45" stop-color="#f2c9d3"/>
        <stop offset="0.8" stop-color="#c9bfb8"/>
        <stop offset="1" stop-color="#eeeaf0"/>
      </radialGradient>
    </defs>
    <circle cx="600" cy="780" r="297" fill="var(--brand-blue)"/>
    <circle cx="600" cy="780" r="280" fill="url(#nest-tones)" role="img" aria-label="Photo of a sleeping newborn curled on pink fur in a woven willow nest"/>
    <circle cx="600" cy="486" r="13" fill="var(--panel-sky)"/>
    <circle cx="600" cy="1074" r="13" fill="var(--panel-sky)"/>
    <circle cx="306" cy="780" r="13" fill="var(--panel-sky)"/>
    <circle cx="894" cy="780" r="13" fill="var(--panel-sky)"/>
  </svg>
</main>
</body>
</html>
```